BOOK COVER (6 X 9) FOR CARNFIELD MOOR BOOKS

Book title: SEASONS OF GLASS; Author: TOMAS R. VELUNDE

This is the story of a man who grew up in Saudi Arabia in the 1940s, was schooled around the world. He survived death many times, once during the revolution in Bangladesh in the 1970s. Although a Pakistani, he knew Saudi royalty and worked there for most of his life. A lot of mystical things happened to him. SORRY TO BE SO VAGUE.

Book size will be 6 x 9

Target Market(s)

Adults interested in immigrant stories; the unexplainable; whimsical memoirs

Requirements
Nice to have
• This is a man who lived in many different worlds and countries. He lived through the Bangladesh revolution and other life threatening events.
Should not have
• Arabic dress -- he wore white suits

```html
<!DOCTYPE html>
<html lang="en">
<head>
<meta charset="utf-8">
<title>Seasons of Glass — Tomas R. Velunde</title>
<link rel="stylesheet" href="https://fonts.googleapis.com/css2?family=Bodoni+Moda:opsz,wght@6..96,400;6..96,500&display=swap">
<style>
  :root {
    --page-bg: #ffffff;
    --sky-black: #05070f;
    --night-navy: #0d1a3a;
    --horizon-blue: #27497a;
    --land-stone: #6f6c60;
    --land-shadow: #3b3a34;
    --sea-teal: #1f7470;
    --sea-deep: #0f3f45;
    --ground-dark: #1b1d1d;
    --city-glow: rgba(255, 214, 140, 0.55);
    --type-white: #fbfaf6;
    --type-shadow: rgba(0, 0, 0, 0.45);
  }
  * { box-sizing: border-box; margin: 0; padding: 0; }
  html, body {
    width: 1200px;
    height: 938px;
    overflow: hidden;
    background: var(--page-bg);
  }
  .book-cover {
    position: absolute;
    left: 320px;
    top: 49px;
    width: 560px;
    height: 840px;
    overflow: hidden;
    font-family: "Bodoni Moda", "Didot", serif;
    color: var(--type-white);
  }
  .cover-art {
    position: absolute;
    inset: 0;
    background:
      radial-gradient(ellipse 38% 22% at 62% 40%, var(--city-glow), transparent 70%),
      radial-gradient(ellipse 30% 10% at 88% 30%, rgba(40, 150, 140, 0.7), transparent 75%),
      radial-gradient(ellipse 55% 14% at 55% 78%, rgba(31, 116, 112, 0.85), transparent 75%),
      radial-gradient(ellipse 20% 40% at 4% 55%, rgba(31, 116, 112, 0.8), transparent 75%),
      linear-gradient(180deg,
        var(--sky-black) 0%,
        var(--night-navy) 9%,
        var(--horizon-blue) 18%,
        var(--land-stone) 32%,
        var(--land-stone) 55%,
        var(--land-shadow) 68%,
        var(--sea-deep) 78%,
        var(--ground-dark) 92%,
        var(--ground-dark) 100%);
  }
  .cover-title {
    position: absolute;
    left: 0;
    right: 0;
    top: 288px;
    text-align: center;
    font-weight: 400;
    line-height: 1;
    text-shadow: 0 2px 6px var(--type-shadow);
  }
  .title-main {
    display: block;
    font-size: 92px;
    letter-spacing: 1px;
  }
  .title-second-line {
    display: flex;
    justify-content: center;
    align-items: flex-start;
    margin-top: 4px;
  }
  .title-joiner {
    font-size: 46px;
    margin-top: 30px;
    margin-right: 10px;
  }
  .title-last {
    font-size: 122px;
    letter-spacing: 1px;
  }
  .cover-author {
    position: absolute;
    left: 0;
    right: 0;
    top: 768px;
    text-align: center;
    font-size: 42px;
    font-weight: 500;
    letter-spacing: 3px;
    line-height: 1;
    text-shadow: 0 2px 5px var(--type-shadow);
  }
</style>
</head>
<body>
  <main class="book-cover">
    <div class="cover-art" role="img" aria-label="Night-time satellite view of the Arabian Peninsula with glowing city lights, the Red Sea and the Gulf of Aden in teal under a dark blue sky"></div>
    <h1 class="cover-title">
      <span class="title-main">SEASONS</span>
      <span class="title-second-line">
        <span class="title-joiner">OF</span>
        <span class="title-last">GLASS</span>
      </span>
    </h1>
    <p class="cover-author">TOMAS R. VELUNDE</p>
  </main>
</body>
</html>
```